Family Owned and Operated Spray Foam Insulation Company needs a business card design

We're a new company based in the heart of Texas (Fort Worth). We spray foam insulation into residential houses, commercial buildings, metal buildings, etc. Spray foam insulation provides a huge reduction in energy/costs so that is what drives our market. We like the primary colors but are open to suggestions and are coming to the experts for some creativity. I'm attaching a picture of shirt mock up we have with KTL on the front to show what we were leaning towards as well as some business cards that I find striking and memorable. I'm looking for a card that is clean and professional with a bit of edge. Note: My computer won't pull up the color samples below for me to choose so it's in your hands.

Target Market(s)

Professional custom home builders, construction industry, home owners

Industry/Entity Type

Residential

Contact Information for Business Card

Name: Mark Kettle (no title) Phone #: 817-555-0148, address: 4187 larkmoor ave fort worth tx 76109, email: mark@ktlinsulation-example.com, website: ktlinsulation-example.com

Requirements
Must have
• We want the words KTL and Kettle Spray Foam Insulation showcased on the card but hopefully on opposite sides
Should not have
• Any type of spray foam gun or splatter clip art

```html
<!DOCTYPE html>
<html lang="en">
<head>
<meta charset="utf-8">
<title>Kettle Spray Foam Insulation – Business Card</title>
<link rel="stylesheet" href="https://fonts.googleapis.com/css2?family=Dosis:wght@500;600;700&display=swap">
<style>
  :root {
    --brand-blue: #1a6ef5;
    --charcoal: #2f3436;
    --paper: #ffffff;
    --ink-light: #ffffff;
  }
  * { margin: 0; padding: 0; box-sizing: border-box; }
  html, body { width: 1200px; height: 686px; overflow: hidden; background: var(--paper); }
  .card {
    position: relative;
    width: 1200px;
    height: 686px;
    background: var(--paper);
    font-family: "Dosis", "Arial Narrow", sans-serif;
    overflow: hidden;
  }
  .brand-initials {
    position: absolute;
    left: 196px;
    top: 154px;
    width: 160px;
    height: 160px;
    display: flex;
    align-items: center;
    justify-content: center;
    font-size: 66px;
    font-weight: 700;
    color: var(--brand-blue);
    line-height: 1;
    letter-spacing: 1px;
  }
  .brand-name {
    position: absolute;
    left: 383px;
    top: 196px;
    font-size: 56px;
    font-weight: 700;
    color: var(--charcoal);
    line-height: 1;
    white-space: nowrap;
  }
  .bands { position: absolute; left: 0; top: 0; }
  .contact-name {
    position: absolute;
    left: 117px;
    top: 428px;
    font-size: 48px;
    font-weight: 600;
    color: var(--ink-light);
    line-height: 1;
  }
  .contact-line {
    position: absolute;
    display: flex;
    align-items: center;
    color: var(--ink-light);
    font-weight: 500;
    line-height: 1;
    white-space: nowrap;
  }
  .contact-line svg { flex: none; }
  .phone { left: 114px; top: 493px; font-size: 30px; gap: 18px; }
  .email { left: 114px; top: 550px; font-size: 24px; gap: 12px; }
  .address {
    position: absolute;
    left: 958px;
    top: 426px;
    font-size: 30px;
    font-weight: 500;
    color: var(--ink-light);
    line-height: 38px;
    font-style: normal;
    white-space: nowrap;
  }
  .website {
    position: absolute;
    right: 14px;
    top: 556px;
    font-size: 30px;
    gap: 16px;
  }
</style>
</head>
<body>
  <main class="card">
    <p class="brand-initials">KTL</p>
    <h1 class="brand-name">Kettle Spray Foam Insulation</h1>

    <svg class="bands" width="1200" height="686" viewBox="0 0 1200 686" aria-hidden="true">
      <rect x="0" y="402" width="1200" height="6" fill="var(--brand-blue)"/>
      <polygon points="0,417 672,417 494,594 0,594" fill="var(--brand-blue)"/>
      <polygon points="683,417 1200,417 1200,594 505,594" fill="var(--charcoal)"/>
      <rect x="0" y="602" width="1200" height="5" fill="var(--charcoal)"/>
    </svg>

    <h2 class="contact-name">Mark Kettle</h2>

    <p class="contact-line phone">
      <svg width="22" height="30" viewBox="0 0 22 30" aria-hidden="true">
        <path d="M5 1 L10 1 L11 8 L7 10 Q8 17 12 21 L15 18 L20 22 L18 28 Q10 29 5 20 Q1 12 5 1 Z" fill="var(--ink-light)"/>
      </svg>
      817-555-0148
    </p>

    <p class="contact-line email">
      <svg width="36" height="26" viewBox="0 0 36 26" aria-hidden="true">
        <rect x="2" y="2" width="32" height="22" fill="none" stroke="var(--ink-light)" stroke-width="3"/>
        <path d="M2 3 L18 15 L34 3" fill="none" stroke="var(--ink-light)" stroke-width="3"/>
      </svg>
      mark@ktlinsulation-example.com
    </p>

    <address class="address">
      4187 larkmoor ave<br>
      fort worth<br>
      Texas 76109
    </address>

    <p class="contact-line website">
      www.ktlinsulation-example.com
      <svg width="30" height="30" viewBox="0 0 30 30" aria-hidden="true">
        <circle cx="14" cy="14" r="11" fill="none" stroke="var(--ink-light)" stroke-width="2.5"/>
        <ellipse cx="14" cy="14" rx="5" ry="11" fill="none" stroke="var(--ink-light)" stroke-width="2"/>
        <line x1="3" y1="14" x2="25" y2="14" stroke="var(--ink-light)" stroke-width="2"/>
        <path d="M17 15 L28 20 L23 22 L26 28 L24 29 L21 23 L17 26 Z" fill="var(--ink-light)" stroke="var(--charcoal)" stroke-width="1"/>
      </svg>
    </p>
  </main>
</body>
</html>
```